Postcard Flyer For Plumbing Company

We are a p[professional plumbing company in NSW that carry out plumbing, electrical and hot water system work.
i want to send a postcard size flyer 105mm x 148mm to our clients to offer $xx off their next job they book with us.
The front of the flyer needs to say.... Feel The Love WIth $35 Off your Next Job. It needs to include a section where their name and postal address can go (74mm W x 24mm H) on the left hand side of the bottom of the flyer - refer attached example.
The other side of the flyer needs to have a section for text, the offer ($35 or $xx what they get off their next job) and also can use the tag line... Call 1 Number for The Best In 3 Trades - Plumbing, Hot Water & Electrical.
Plumbing, hot water and electrical pictures/icons can be used.
I want the flyer to stand out, use the corporate colours and be modern whilst letting them know that they can use this voucher on their next job.
Refer attachments.

Target Market(s)

Homeowners and our existing clients

Industry/Entity Type

Plumbing

Font styles to use
Serif

Colors
0255a3
ec1f27
ffffff
d3d3d3

Requirements
Must have
• Corporate colours and logos
• Red Colour:
• C=0
• M=100
• Y=100
• K=0
• Blue Colour
• C= 100
• M=66
• Y=0
• K=2
• Grey Colour
• C= 26
• M=21
• Y=19
• K=0
Nice to have
• predominately white background
Should not have
• Black background and lots of black.

```html
<!DOCTYPE html>
<html lang="en">
<head>
<meta charset="utf-8">
<title>Feel The Love Postcard</title>
<link href="https://fonts.googleapis.com/css2?family=Montserrat:wght@300;400;600;800&display=swap" rel="stylesheet">
<style>
  :root {
    --stage: #070808;
    --red: #ec1f27;
    --red-deep: #e10b12;
    --blue: #0255a3;
    --grey: #d3d3d3;
    --fold-grey: #d9dcdb;
    --white: #ffffff;
    --ink: #111111;
  }
  * { margin: 0; padding: 0; box-sizing: border-box; }
  html, body {
    width: 1200px; height: 1200px; overflow: hidden;
    background: var(--stage);
    font-family: "Montserrat", Arial, sans-serif;
  }
  .postcard {
    position: absolute; left: 182px; top: 313px;
    width: 838px; height: 602px;
    background: var(--white); overflow: hidden;
  }
  .postcard__shapes { position: absolute; inset: 0; }
  .headline {
    position: absolute; left: 220px; top: 62px;
    color: var(--white); line-height: 1; letter-spacing: -0.04em;
  }
  .headline__line { display: block; white-space: nowrap; }
  .headline__light { font-weight: 300; font-size: 60px; }
  .headline__bold { font-weight: 800; font-size: 84px; }
  .headline .l1 { height: 56px; }
  .headline .l2 { height: 70px; }
  .headline .l3 { height: 72px; }
  .address-box {
    position: absolute; left: 66px; top: 414px;
    width: 402px; height: 130px;
    border: 2px solid var(--fold-grey); border-radius: 18px;
  }
  .address-box__line {
    position: absolute; left: 31px; right: 39px; height: 2px;
    background: var(--fold-grey);
  }
  .brand {
    position: absolute; left: 534px; top: 455px; width: 240px;
    text-align: center;
  }
  .brand__name {
    font-weight: 800; font-size: 34px; color: var(--blue);
    letter-spacing: -0.02em; line-height: 1;
    display: inline-flex; align-items: center; gap: 8px;
  }
  .brand__dot {
    width: 14px; height: 14px; border-radius: 50%; background: var(--red);
  }
  .brand__services {
    margin-top: 24px; font-weight: 600; font-size: 14px; color: var(--ink);
    white-space: nowrap;
  }
</style>
</head>
<body>
  <div class="postcard">
    <svg class="postcard__shapes" width="838" height="602" viewBox="0 0 838 602">
      <polygon class="fold-shadow" points="838,122 718,335 386,379 0,380 0,370 690,327" fill="var(--fold-grey)"/>
      <polygon class="hero-band" points="0,0 838,0 838,122 690,327 0,377" fill="var(--red)"/>
      <rect class="tradesperson-art" x="0" y="23" width="186" height="354" fill="var(--red-deep)" role="img" aria-label="Illustration of a tradesperson wearing a hard hat, in white line art"/>
    </svg>

    <div class="headline">
      <span class="headline__line headline__light l1">FEEL THE LOVE</span>
      <span class="headline__line l2"><span class="headline__light">WITH </span><span class="headline__bold">$35 OFF</span></span>
      <span class="headline__line headline__bold l3">YOUR NEXT</span>
      <span class="headline__line headline__bold">JOB</span>
    </div>

    <div class="address-box" aria-label="Recipient name and postal address">
      <div class="address-box__line" style="top:31px"></div>
      <div class="address-box__line" style="top:63px"></div>
      <div class="address-box__line" style="top:94px"></div>
    </div>

    <div class="brand">
      <div class="brand__name"><span class="brand__dot"></span>Harbour Trades</div>
      <div class="brand__services">Plumbing • Electrical • Hot Water</div>
    </div>
  </div>
</body>
</html>
```